School Learner profile graphic representation

I have a set of ideas around communicating our school 'learner profile'. These represent the attitudes, habits and dispositions we are trying to develop through our curriculum and wider enrichment programme. I want the links between the ideas and concepts to be represented in some form of an inforgraphic which can be published and displayed for the whole community to connect with. we run two schools and want the profile to represent for both.

Target Market(s)

Students, Parents, Teachers, Wider community in education

Industry/Entity Type

Education

Font styles to use
Other font styles liked:
• Johnson p22

Colors

Designer to choose colors to be used in the design.

Requirements
Must have
• See my diagram in the ppt.
• The statements Aspiration, Agency, Agility, Altitude with the supporting descriptions. Ideally the values in the center is also represented. The two school logos should also be present somehow (both emblems at least). Let me know if the full logo files are required
Nice to have
• the numbering shown in my diagram is not absolutely necessary is it is not necessarily a linear process and rather cyclical and cross reinforcing

```html
<!DOCTYPE html>
<html lang="en">
<head>
<meta charset="utf-8">
<title>Envisioning our Learners</title>
<link href="https://fonts.googleapis.com/css2?family=Inter:wght@700;800&family=Nunito:wght@600;700&display=swap" rel="stylesheet">
<style>
  :root {
    --brand-red: #c8040a;
    --panel: #f3f3f4;
    --white: #ffffff;
    --ink: #2b2b2b;
    --muted: #555555;
    --agility: #b5121b;
    --altitude: #6cb52d;
    --aspiration: #1bb3a6;
    --agency: #1a7fc9;
  }
  * { margin: 0; padding: 0; box-sizing: border-box; }
  html, body { width: 848px; height: 1200px; overflow: hidden; background: var(--white); }
  .poster { position: relative; width: 848px; height: 1200px; overflow: hidden; background: var(--white); font-family: "Nunito", sans-serif; }
  .hero-band { position: absolute; left: 0; top: 0; width: 848px; height: 1030px; background: var(--brand-red); }
  .content-panel { position: absolute; left: 47px; top: 346px; width: 754px; height: 684px; background: var(--panel); border-radius: 10px 10px 0 0; }
  .title { position: absolute; color: var(--white); font-family: "Inter", sans-serif; font-weight: 800; letter-spacing: -2.5px; line-height: 1; }
  .title-main { left: 52px; top: 156px; font-size: 68px; }
  .title-our { left: 44px; top: 252px; font-size: 34px; font-weight: 700; letter-spacing: -1px; text-decoration: underline; text-decoration-thickness: 3px; text-underline-offset: 5px; }
  .title-learners { left: 124px; top: 252px; font-size: 68px; }
  .student-photo { position: absolute; left: 440px; top: 52px; width: 380px; height: 501px; border-radius: 180px 180px 16px 16px; background: linear-gradient(175deg, #8a5a3c 0%, #e07a64 40%, #d96a56 70%, #3d5f8f 100%); }
  .flow { position: absolute; left: 0; top: 0; width: 848px; height: 1200px; }
  .trait { position: absolute; width: 170px; }
  .trait h2 { font-family: "Nunito", sans-serif; font-weight: 700; font-size: 17px; letter-spacing: -0.3px; margin-bottom: 4px; }
  .trait p { font-size: 12px; line-height: 15.5px; color: var(--ink); font-weight: 600; }
  .trait-left { text-align: right; }
  .trait-agility { left: 80px; top: 478px; }
  .trait-agility h2 { color: var(--agility); }
  .trait-altitude { left: 597px; top: 577px; }
  .trait-altitude h2 { color: var(--altitude); }
  .trait-aspiration { left: 80px; top: 694px; }
  .trait-aspiration h2 { color: var(--aspiration); }
  .trait-agency { left: 597px; top: 801px; }
  .trait-agency h2 { color: var(--agency); }
  .footer-rule { position: absolute; left: 106px; top: 1029px; width: 636px; height: 2px; background: var(--brand-red); }
  .school { position: absolute; top: 1080px; display: flex; align-items: center; gap: 12px; }
  .school-dot { width: 52px; height: 52px; border-radius: 50%; background: var(--brand-red); flex: none; }
  .school-private { left: 85px; }
  .school-community { left: 594px; }
  .school-name { font-family: "Nunito", sans-serif; font-weight: 700; font-size: 18px; color: var(--ink); line-height: 1.2; }
  .school-note { font-family: "Nunito", sans-serif; font-weight: 600; font-size: 12px; color: var(--muted); margin-top: 3px; }
</style>
</head>
<body>
<div class="poster">
  <div class="hero-band"></div>
  <div class="content-panel"></div>

  <div class="title title-main">Envisioning</div>
  <div class="title title-our">our</div>
  <div class="title title-learners">Learners</div>

  <div class="student-photo" role="img" aria-label="Photo of a cheerful student holding a blue notebook and raising her arm in celebration"></div>

  <svg class="flow" viewBox="0 0 848 1200" aria-hidden="true">
    <defs>
      <linearGradient id="connector" x1="0" y1="513" x2="0" y2="840" gradientUnits="userSpaceOnUse">
        <stop offset="0" stop-color="#b5121b"/>
        <stop offset="0.3" stop-color="#6cb52d"/>
        <stop offset="0.65" stop-color="#1bb3a6"/>
        <stop offset="1" stop-color="#1a7fc9"/>
      </linearGradient>
      <filter id="soft-shadow" x="-40%" y="-40%" width="180%" height="180%">
        <feDropShadow dx="0" dy="6" stdDeviation="6" flood-color="#000" flood-opacity="0.22"/>
      </filter>
    </defs>

    <path d="M322 446 H140 A67 67 0 0 0 140 580 H322" fill="none" stroke="#b5121b" stroke-width="1.4"/>
    <path d="M511 555 H696 A67 67 0 0 1 696 689 H511" fill="none" stroke="#6cb52d" stroke-width="1.4"/>
    <path d="M322 664 H140 A67 67 0 0 0 140 798 H322" fill="none" stroke="#1bb3a6" stroke-width="1.4"/>
    <path d="M511 772 H696 A67 67 0 0 1 696 906 H511" fill="none" stroke="#1a7fc9" stroke-width="1.4"/>

    <path d="M322 513 C430 513 410 622 511 622 C410 622 430 731 322 731 C430 731 410 840 511 840" fill="none" stroke="url(#connector)" stroke-width="38" stroke-linejoin="round"/>

    <g fill="none" stroke="#ffffff" stroke-width="1.6" stroke-linecap="round" stroke-linejoin="round">
      <path d="M398 555 L438 580 M430 570 L438 580 L425 582"/>
      <path d="M438 666 L398 690 M411 689 L398 690 L405 680"/>
      <path d="M398 773 L438 798 M430 788 L438 798 L425 800"/>
    </g>

    <circle cx="322" cy="513" r="64" fill="#b5121b"/>
    <circle cx="322" cy="513" r="59" fill="#f4f4f4" filter="url(#soft-shadow)"/>
    <circle cx="511" cy="622" r="64" fill="#6cb52d"/>
    <circle cx="511" cy="622" r="59" fill="#f4f4f4" filter="url(#soft-shadow)"/>
    <circle cx="322" cy="731" r="64" fill="#1bb3a6"/>
    <circle cx="322" cy="731" r="59" fill="#f4f4f4" filter="url(#soft-shadow)"/>
    <circle cx="511" cy="840" r="64" fill="#1a7fc9"/>
    <circle cx="511" cy="840" r="59" fill="#f4f4f4" filter="url(#soft-shadow)"/>

    <path d="M322 486 C334 500 344 510 342 526 C340 538 332 544 322 544 C311 544 302 537 302 525 C302 514 310 508 313 500 C316 508 318 512 322 514 C324 504 325 494 322 486 Z" fill="#d2202a"/>
    <path d="M322 544 C314 544 309 538 310 530 L322 520 L334 530 C335 538 330 544 322 544 Z" fill="#a5121a"/>

    <path d="M484 636 L502 598 L512 616 L520 604 L540 636 Z" fill="#8b4a3a"/>
    <path d="M502 598 L497 610 L507 608 Z M520 604 L516 611 L525 611 Z" fill="#ffffff"/>
    <rect x="482" y="635" width="60" height="4" rx="2" fill="#6cb52d"/>
    <circle cx="494" cy="588" r="6" fill="#cfe4f2"/>

    <circle cx="322" cy="733" r="25" fill="#1bb3a6"/>
    <circle cx="322" cy="733" r="18" fill="#ffffff"/>
    <circle cx="322" cy="733" r="11" fill="#7fd3e6"/>
    <circle cx="322" cy="733" r="4" fill="#1a4f7a"/>
    <path d="M322 733 L348 708" stroke="#3a3a3a" stroke-width="2"/>
    <path d="M344 704 L354 700 L350 712 Z" fill="#e0303a"/>

    <path d="M494 850 C482 850 478 836 488 831 C487 820 500 814 507 821 C512 810 530 812 530 826 C540 826 542 842 532 850" fill="none" stroke="#1a7fc9" stroke-width="3.4" stroke-linecap="round"/>
    <g stroke="#1a7fc9" stroke-width="3" stroke-linecap="round">
      <path d="M505 832 V866 M517 832 V866"/>
      <path d="M505 842 H517 M505 852 H517 M505 862 H517"/>
    </g>
  </svg>

  <div class="trait trait-left trait-agility">
    <h2>Agility</h2>
    <p>Are determined, equipped<br>and able to accomplish<br>great things</p>
  </div>
  <div class="trait trait-altitude">
    <h2>Altitude</h2>
    <p>Achieve great things<br>and work to elevate<br>others</p>
  </div>
  <div class="trait trait-left trait-aspiration">
    <h2>Aspiration</h2>
    <p>Inspired and believe<br>in pursuing great<br>things</p>
  </div>
  <div class="trait trait-agency">
    <h2>Agency</h2>
    <p>Believe in their capacity<br>and responsibility to do<br>great things.</p>
  </div>

  <div class="footer-rule"></div>

  <div class="school school-private">
    <span class="school-dot"></span>
    <div>
      <div class="school-name">Al Noor Private School</div>
      <div class="school-note">Learning with heart, every day</div>
    </div>
  </div>

  <div class="school school-community">
    <span class="school-dot"></span>
    <div class="school-name">Al Noor Community School</div>
  </div>
</div>
</body>
</html>
```